Larkfield Clinic Marketing Flyer

We are a new medical practice in the community and need a flyer to send to other medical offices to inform of our services. We just completed our logo with PixelGuild and would like to incorporate that plus our marketing content into the flyer. Our medical practice has 2 divisions: (1)Mental Health/Psychiatry and (2) Migraine and Neurospasticity Management. Please see website for content and provider photos at www.LarkfieldCare.example

Target Market(s)

Other Healthcare Professionals in the Community

Industry/Entity Type

Medical

Requirements
Must have
• Photos of all 5 healthcare providers, phone number, address, logo

```html
<!DOCTYPE html>
<html lang="en">
<head>
<meta charset="utf-8">
<title>Larkfield Clinic Flyer</title>
<link rel="stylesheet" href="https://fonts.googleapis.com/css2?family=Playfair+Display:ital,wght@0,700;1,500&family=Raleway:wght@400;500;600&display=swap">
<style>
:root{
  --backdrop:#1b2530;
  --paper:#ffffff;
  --teal:#17968a;
  --ink:#1d1d1d;
  --ink-soft:#2a2a2a;
  --rule:#8a8a8a;
  --white:#ffffff;
}
*{box-sizing:border-box;margin:0;padding:0}
html,body{width:1200px;height:849px;overflow:hidden;background:var(--backdrop)}
.flyer{position:absolute;left:314px;top:20px;width:572px;height:809px;background:var(--paper);font-family:'Raleway',sans-serif;color:var(--ink)}
.hero{position:absolute;left:0;top:0;width:572px;height:286px;overflow:hidden}
.hero-photo{position:absolute;inset:0;background:linear-gradient(100deg,#3b4a36 0%,#1f281e 38%,#262d22 60%,#4c4234 80%,#6e6450 100%)}
.headline{position:absolute;left:52px;top:44px;font-family:'Playfair Display',serif;font-weight:700;font-size:47px;line-height:55px;color:var(--white)}
.tagline{position:absolute;left:52px;top:218px;font-family:'Playfair Display',serif;font-style:italic;font-weight:500;font-size:20px;line-height:27px;color:var(--white)}
.division-band{position:absolute;left:0;top:286px;width:572px;height:48px;background:var(--teal)}
.division-title{position:absolute;font-weight:500;font-size:13.5px;line-height:16px;color:var(--ink)}
.division-title.left{left:52px;top:17px}
.division-title.right{left:293px;top:9px}
.col-text{position:absolute;font-size:10.3px;line-height:12.7px;text-align:justify;hyphens:auto;-webkit-hyphens:auto;color:var(--ink-soft)}
.mh-intro{left:52px;top:345px;width:228px}
.mg-intro{left:293px;top:345px;width:228px}
.provider{position:absolute;width:106px}
.provider .photo{width:106px;height:121px;background:linear-gradient(160deg,#8f9aa3,#4e5a63)}
.provider .name{margin-top:5px;font-weight:600;font-size:10.6px;line-height:12.7px}
.provider .cred{font-size:10.3px;line-height:12.7px}
.physician{position:absolute;left:293px;top:444px;width:228px;font-size:10.3px;line-height:12.7px;text-align:justify;hyphens:auto;-webkit-hyphens:auto;color:var(--ink-soft)}
.physician .photo{float:right;width:106px;height:121px;margin:0 0 0 13px;background:linear-gradient(160deg,#8a6e52,#c9b191)}
.divider{position:absolute;left:293px;top:607px;width:228px;height:1px;background:var(--rule)}
.brand{position:absolute;left:293px;top:614px;width:228px;text-align:center}
.brand .mark{display:block;width:26px;height:26px;margin:0 auto 4px;border-radius:50%;background:var(--teal)}
.brand .name{font-weight:600;font-size:13.5px;letter-spacing:1px;color:var(--teal)}
.info{position:absolute;top:686px;font-size:10.3px;line-height:12.7px;color:var(--ink-soft)}
.info h3{font-weight:600;font-size:10.6px;margin-bottom:5px;color:var(--ink)}
.info p{margin-bottom:5px}
.contact{left:293px}
.locations{left:446px;width:90px}
.footer-band{position:absolute;left:0;bottom:0;width:572px;height:16px;background:var(--teal)}
</style>
</head>
<body>
<main class="flyer">
  <section class="hero">
    <div class="hero-photo" role="img" aria-label="Hero photo of a smiling young woman outdoors against blurred greenery"></div>
    <h1 class="headline">Helping Bodies<br>Helping Minds<br>Helping You</h1>
    <p class="tagline">Mental Health and Psychiatry Services<br>Migraine and Neurospasticity Intervention</p>
  </section>

  <div class="division-band">
    <h2 class="division-title left">Mental Health/Psychiatry</h2>
    <h2 class="division-title right">Migraine and Neurospasticity<br>Management</h2>
  </div>

  <p class="col-text mh-intro">Bringing comprehensive evaluation, medication management and psychotherapy to the full spectrum of mental health disorders including minor, moderate and major depression, bipolar disorder, ADD/ADHD, anxiety, schizophrenia, stress or grief reactions, and others.</p>

  <p class="col-text mg-intro">Injections of botulinum neurotoxin are a widely used therapeutic form of treatment for both chronic migraines and patients with involuntary muscle contractions (neurospasticity). Injections may offer up to 3 months of relief and may be combined with other pharmaceutical interventions for maximum benefit.</p>

  <div class="provider" style="left:52px;top:443px">
    <div class="photo" role="img" aria-label="Portrait of provider Evan Marlow"></div>
    <div class="name">Evan Marlow</div><div class="cred">PMHNP - BC</div>
  </div>
  <div class="provider" style="left:173px;top:443px">
    <div class="photo" role="img" aria-label="Portrait of provider Dana Whitcomb"></div>
    <div class="name">Dana Whitcomb</div><div class="cred">PMHNP - BC</div>
  </div>
  <div class="provider" style="left:52px;top:612px">
    <div class="photo" role="img" aria-label="Portrait of provider Carl Brennick"></div>
    <div class="name">Carl Brennick</div><div class="cred">PMHNP - BC</div>
  </div>
  <div class="provider" style="left:173px;top:612px">
    <div class="photo" role="img" aria-label="Portrait of provider Ruth Ellison"></div>
    <div class="name">Ruth Ellison</div><div class="cred">PMHNP - BC</div>
  </div>

  <div class="physician">
    <div class="photo" role="img" aria-label="Portrait of Dr. Neil Hartwell"></div>
    A board certified family practice physician, Dr. Neil Hartwell has incorporated botulinum toxin injections into his practice for several years. Now retired from family medicine, he is devoted to helping patients find relief from migraines and muscle spasticity issues.
  </div>

  <div class="divider"></div>

  <div class="brand">
    <span class="mark"></span>
    <span class="name">LARKFIELD CLINIC</span>
  </div>

  <div class="info contact">
    <h3>Contact</h3>
    <p>Mental Health<br>Phone (555)014-2260</p>
    <p>Migraine and<br>Neurospasticity<br>Phone (555) 014-2291</p>
  </div>
  <div class="info locations">
    <h3>Locations</h3>
    <p>Larkfield<br>Clinic<br>215 W. Alder Lane, Suite B Millbrook, ID 83000</p>
  </div>

  <div class="footer-band"></div>
</main>
</body>
</html>
```